Mejorar diseño web de www.velbio.es

I need to improve the graphic design of www.velbio.es to look more professional and much better visually than it already is, I think some texts are confused with the colors of the image, are not clear or visible, for the PC version , mobile and tablet.

I DO NOT NEED WEB DESIGN. I just need to redesign the body of each page, I mean the images and the text that there is about them.

The upper and lower menus do not want to touch them (bara and buttons).

I need to change the images currently present on the page www.velbio.es (Jardinera, Piscinas) for the images that I have uploaded here Gardening and Swimming Pools.

Any questions or questions let me know. Thank you.

___________

Necesito mejorar el diseño gráfico de www.velbio.es para que parezca mas profesional y mucho mejor visualmente de lo que ya es, me parece que algunos textos se confunden con los colores de la imagen, no son claros ni visibles, para la version PC, movil y tablet.

NO NECESITO DISEÑO WEB. Solamente necesito rediseñar el cuerpo de cada pagina, me refiero a las imágenes y al texto que hay sobre ellas.

Los menus superiores e inferiores no quiero tocarlos (bara y botones).

Necesito cambiar las imagenes presentes actualmente en la pagina www.velbio.es (Jardinera, Piscinas) por las imágenes que he subido aquí Jardinería y Piscinas.

Cualquier duda o pregunta hacedmelo saber. Gracias.

```html
<!DOCTYPE html>
<html lang="es">
<head>
<meta charset="utf-8">
<title>Velbio · Piscinas</title>
<link href="https://fonts.googleapis.com/css2?family=Open+Sans:wght@400;600;700;800&display=swap" rel="stylesheet">
<style>
:root{
  --brand-blue:#1c5b8f;
  --nav-blue:#1683c2;
  --nav-blue-dark:#0f6aa3;
  --nav-active:#3fa6dc;
  --green:#2fb34a;
  --green-dark:#22933a;
  --accent-green:#8fd14f;
  --hero-green:#3a6344;
  --hero-blue:#1f7fae;
  --ink:#2d3a46;
  --muted:#7a8794;
  --white:#ffffff;
}
*{box-sizing:border-box;margin:0;padding:0}
html,body{width:1200px;height:800px;overflow:hidden;background:var(--white);font-family:"Open Sans",Arial,sans-serif;color:var(--ink)}
.page{position:relative;width:1200px;height:800px}
.site-header{height:67px;border-top:3px solid var(--nav-blue);display:flex;align-items:center;padding:0 0 0 240px;gap:46px}
.brand{display:flex;align-items:center;gap:8px;margin-right:34px}
.brand-mark{width:16px;height:16px;background:var(--green)}
.brand-name{font-weight:800;font-size:34px;color:var(--brand-blue);letter-spacing:-.5px}
.contact{display:flex;align-items:center;gap:9px}
.contact svg{width:24px;height:24px}
.contact-label{font-size:8px;color:var(--muted);line-height:1}
.contact-value{font-size:13px;font-weight:700;color:var(--ink);line-height:1.2}
.social{display:flex;gap:6px;margin-left:10px}
.social span{width:16px;height:16px;border-radius:50%;background:var(--nav-blue)}
.main-nav{height:22px;background:linear-gradient(var(--nav-blue),var(--nav-blue-dark));display:flex;justify-content:center}
.main-nav a{display:block;width:92px;text-align:center;font-size:8.5px;font-weight:600;color:var(--white);line-height:22px;text-decoration:none}
.main-nav a.is-active{background:var(--nav-active);border-bottom:2px solid var(--accent-green)}
.hero{position:relative;height:322px;overflow:hidden}
.hero-photo{position:absolute;inset:0;background:linear-gradient(160deg,var(--hero-green) 0%,var(--hero-blue) 100%)}
.hero-content{position:absolute;left:62px;top:14px;width:640px;color:var(--white);text-shadow:0 1px 2px rgba(0,0,0,.45)}
.hero-title{font-size:18.5px;font-weight:800;line-height:1.2;white-space:nowrap;letter-spacing:-.2px}
.hero-subtitle{display:inline-block;font-size:14.5px;font-weight:700;line-height:1.3;border-bottom:2px solid var(--accent-green);padding-bottom:3px;margin-bottom:12px}
.service-list{list-style:none;margin:0 0 10px 30px}
.service-list li{font-size:10.5px;font-weight:600;line-height:17px;display:flex;align-items:center;gap:8px}
.service-list li::before{content:"";width:6px;height:6px;border-radius:50%;background:var(--white)}
.offer-box{border:1.5px solid var(--white);background:rgba(0,0,0,.25);padding:6px 10px;font-size:10px;font-weight:600;line-height:16px;width:480px;margin:0 0 14px 0}
.quote-line{display:flex;gap:36px;font-size:12.5px;font-weight:700;margin-left:30px}
.site-footer{height:21px;background:linear-gradient(var(--green),var(--green-dark));display:flex;align-items:center;justify-content:center;gap:14px;font-size:7.5px;color:var(--white)}
.site-footer .sep{opacity:.7}
.site-footer .copy{margin-left:70px}
.chat-button{position:absolute;left:1068px;top:707px;width:96px;height:20px;background:var(--green);color:var(--white);font-size:8px;font-weight:700;display:flex;align-items:center;justify-content:center;gap:5px;border-radius:2px}
.chat-button svg{width:9px;height:9px}
</style>
</head>
<body>
<div class="page">
  <header class="site-header">
    <div class="brand"><span class="brand-mark"></span><span class="brand-name">Velbio</span></div>
    <div class="contact">
      <svg viewBox="0 0 24 24"><circle cx="12" cy="12" r="11" fill="none" stroke="#1683c2" stroke-width="1.5"/><path d="M8.5 7c.8-.6 1.5-.3 1.9.5l.7 1.5c.2.6 0 1-.4 1.3l-.6.5c.6 1.4 1.6 2.4 3 3l.5-.6c.3-.4.8-.6 1.3-.4l1.5.7c.8.4 1.1 1.1.5 1.9-1 1.3-2.6 1.4-4.3.5A10 10 0 0 1 8 11.3C7.2 9.6 7.3 8 8.5 7z" fill="#1683c2"/></svg>
      <div><div class="contact-label">Llámanos</div><div class="contact-value">910 555 034</div></div>
    </div>
    <div class="contact">
      <svg viewBox="0 0 24 24"><circle cx="12" cy="12" r="11" fill="none" stroke="#2fb34a" stroke-width="1.5"/><rect x="9" y="6" width="6" height="12" rx="1" fill="none" stroke="#2fb34a" stroke-width="1.5"/><circle cx="12" cy="16" r=".8" fill="#2fb34a"/></svg>
      <div><div class="contact-label">Móvil</div><div class="contact-value">644 555 604</div></div>
    </div>
    <div class="contact">
      <svg viewBox="0 0 24 24"><circle cx="12" cy="12" r="11" fill="none" stroke="#1683c2" stroke-width="1.5"/><rect x="7" y="8" width="10" height="8" fill="none" stroke="#1683c2" stroke-width="1.5"/><path d="M7 8l5 4 5-4" fill="none" stroke="#1683c2" stroke-width="1.5"/></svg>
      <div><div class="contact-label">Escríbenos</div><div class="contact-value">CONTACTO</div></div>
    </div>
    <div class="social" aria-label="Redes sociales"><span></span><span></span><span></span><span></span><span></span><span></span></div>
  </header>

  <nav class="main-nav">
    <a href="#">INICIO</a><a href="#">CONSTRUCCIÓN</a><a href="#">REFORMAS</a><a href="#">LIMPIEZA</a><a href="#">JARDINERÍA</a><a href="#" class="is-active">PISCINAS</a><a href="#">CCTV</a><a href="#">BLOG</a>
  </nav>

  <section class="hero">
    <div class="hero-photo" role="img" aria-label="Fotografía de piscina comunitaria con tumbonas, sombrilla y seto"></div>
    <div class="hero-content">
      <h1 class="hero-title">SERVICIO DE MANTENIMIENTO Y LIMPIEZA DE PISCINAS</h1>
      <h2 class="hero-subtitle">CUIDAMOS Y MANTENEMOS LA PISCINA DE SU COMUNIDAD</h2>
      <ul class="service-list">
        <li>Limpieza y desinfección de vaso</li>
        <li>Llenado y tratamiento del agua</li>
        <li>Tramitación de la documentación para la apertura de temporada</li>
        <li>Mantenimiento y tratamiento químico del agua</li>
        <li>Servicio de socorristas en varios turnos y horarios</li>
        <li>Mantenimiento y reparación de las máquinas de la piscina</li>
      </ul>
      <p class="offer-box">Ahorre dinero y gane calidad y confianza contratando también otros servicios nuestros. Además, obtendrá un 5% descuento al realizar cualquier reforma de su comunidad o de alguna vivienda ubicada en la misma solo por tener contratado el servicio de PISCINAS.</p>
      <div class="quote-line"><span>¿Ya tiene un presupuesto?</span><span>Envíenoslo e intentaremos mejorarlo</span></div>
    </div>
  </section>

  <footer class="site-footer">
    <span>Legal</span><span class="sep">|</span><span>Cookies</span><span class="sep">|</span><span>Contacto</span><span class="sep">|</span><span>Empresas</span><span class="sep">|</span><span>Trabaja con nosotros</span><span class="sep">|</span><span>Sobre nuestros servicios</span>
    <span class="copy">© 2016 Velbio.es</span>
  </footer>

  <div class="chat-button">
    <svg viewBox="0 0 10 10"><path d="M1 1h8v6H4L2 9V7H1z" fill="#fff"/></svg>Iniciar Chat
  </div>
</div>
</body>
</html>
```